Letterhead to Introduce a 'Sister' Company.

What I am needing is a design for a letter head to introduce our current customers base of (KT Alarm) customers to our new service, 'Kestrel Tide Solar Brokers'

```html
<!DOCTYPE html>
<html lang="en">
<head>
<meta charset="utf-8">
<title>Kestrel Tide Solar Brokers – Letterhead</title>
<link href="https://fonts.googleapis.com/css2?family=Open+Sans:wght@400;600;700&family=Lato:wght@400&family=Arimo:wght@400&display=swap" rel="stylesheet">
<style>
  :root{
    --navy:#0c4a87;
    --orange:#f7990c;
    --sun-light:#ffc15a;
    --ink:#3d3d3d;
    --paper:#ffffff;
    --green:#3aa935;
  }
  html,body{margin:0;padding:0;overflow:hidden;background:var(--paper);}
  .letterhead{position:relative;width:1040px;height:1200px;overflow:hidden;background:var(--paper);font-family:"Open Sans",sans-serif;color:var(--ink);}
  .header-swoosh,.footer-band{position:absolute;left:0;width:1040px;}
  .header-swoosh{top:0;height:240px;}
  .footer-band{bottom:0;height:240px;}

  .brand{position:absolute;left:95px;top:78px;width:250px;text-align:center;}
  .brand-mark{display:block;width:58px;height:58px;border-radius:50%;background:var(--orange);margin:0 auto 10px;}
  .brand-name{font-weight:700;font-size:27px;letter-spacing:.5px;color:var(--navy);line-height:1;white-space:nowrap;}
  .brand-tag{display:flex;align-items:center;gap:6px;margin-top:6px;font-weight:600;font-size:12px;letter-spacing:2px;color:var(--orange);}
  .brand-tag::before,.brand-tag::after{content:"";flex:1;height:2px;background:var(--orange);}

  .contact{position:absolute;left:675px;top:72px;padding-left:14px;border-left:1px solid #b9b9b9;font-family:"Arimo",sans-serif;font-size:17px;color:#1b2d4a;line-height:22px;}
  .contact-item{display:flex;align-items:center;gap:6px;white-space:nowrap;}
  .contact-item svg{width:13px;height:13px;fill:var(--navy);flex:none;}

  .letter{position:absolute;left:97px;top:214px;width:842px;font-size:15.5px;}
  .letter p{margin:0;}
  .issue-date{margin-bottom:17px !important;}
  .recipient{line-height:18px;margin-bottom:50px !important;}
  .salutation{margin-bottom:26px !important;}
  .body-copy{line-height:27px;text-align:justify;margin-bottom:27px !important;}
  .closing{margin-top:52px !important;}
  .signatory{margin-top:56px !important;font-size:19px;font-weight:600;color:#2c2c2c;}
  .role{margin-top:6px !important;font-size:15.5px;}

  .sister-brand{position:absolute;left:0;width:1040px;top:1102px;text-align:center;font-weight:700;font-size:36px;color:var(--navy);letter-spacing:1px;}
  .address{position:absolute;left:0;width:1040px;top:1164px;text-align:center;font-family:"Lato",sans-serif;font-size:19px;color:#fff;}
</style>
</head>
<body>
<main class="letterhead">
  <svg class="header-swoosh" viewBox="0 0 1040 240" aria-hidden="true">
    <path d="M0,0 H840 C620,4 440,14 330,40 C170,80 40,140 0,235 Z" fill="var(--navy)"/>
  </svg>

  <div class="brand">
    <span class="brand-mark"></span>
    <div class="brand-name">KESTREL TIDE</div>
    <div class="brand-tag">SOLAR BROKERS</div>
  </div>

  <div class="contact">
    <div class="contact-item"><svg viewBox="0 0 24 24"><path d="M6.6 10.8a15 15 0 0 0 6.6 6.6l2.2-2.2c.3-.3.7-.4 1-.2 1.1.4 2.3.6 3.6.6.6 0 1 .4 1 1V20c0 .6-.4 1-1 1A17 17 0 0 1 3 4c0-.6.4-1 1-1h3.5c.6 0 1 .4 1 1 0 1.3.2 2.5.6 3.6.1.3 0 .7-.2 1z"/></svg>061-482 730 915</div>
    <div class="contact-item"><svg viewBox="0 0 24 24"><path d="M7 1h10a2 2 0 0 1 2 2v18a2 2 0 0 1-2 2H7a2 2 0 0 1-2-2V3a2 2 0 0 1 2-2zm0 3v14h10V4zm5 15.5a1 1 0 1 0 0 2 1 1 0 0 0 0-2z"/></svg>061-482 730 916</div>
    <div class="contact-item"><svg viewBox="0 0 24 24"><path d="M2 5h20v14H2zm2 2v.5l8 5 8-5V7zm0 2.8V17h16V9.8l-8 5z"/></svg>hello@kestreltide.com</div>
    <div class="contact-item"><svg viewBox="0 0 24 24"><path d="M12 2a10 10 0 1 0 0 20 10 10 0 0 0 0-20zm6.9 6h-2.9a15 15 0 0 0-1.4-3.6A8 8 0 0 1 18.9 8zM12 4c.8 1.2 1.5 2.5 1.9 4h-3.8c.4-1.5 1.1-2.8 1.9-4zM4.3 14a8 8 0 0 1 0-4h3.4a16 16 0 0 0 0 4zm.8 2h2.9c.3 1.3.8 2.5 1.4 3.6A8 8 0 0 1 5.1 16zM8 8H5.1a8 8 0 0 1 4.3-3.6C8.8 5.5 8.3 6.7 8 8zm4 12c-.8-1.2-1.5-2.5-1.9-4h3.8c-.4 1.5-1.1 2.8-1.9 4zm2.3-6H9.7a14 14 0 0 1 0-4h4.6a14 14 0 0 1 0 4zm.3 5.6c.6-1.1 1.1-2.3 1.4-3.6h2.9a8 8 0 0 1-4.3 3.6zm1.7-5.6a16 16 0 0 0 0-4h3.4a8 8 0 0 1 0 4z"/></svg>www.kestreltide.com</div>
  </div>

  <article class="letter">
    <p class="issue-date">Issuing Date: May 5, 2018</p>
    <p class="recipient">Name Of Employee Mr. XYZABC<br>Address of Employee<br>Address Line 2 etc..</p>
    <p class="salutation">Dear Mr.XYZABC</p>
    <p class="body-copy">Lorem Ipsum has been the industry's standard dummy text ever since the 1500s, when an unknown printer took a galley of type and scrambled it to make a type specimen book. It has survived not only five centuries, but also the leap into electronic typesetting, remaining essentially unchanged. It was popularised in the 1960s with the release of Letraset sheets containing Lorem Ipsum passages, and more recently with desktop publishing software like Aldus PageMaker including versions of Lorem Ipsum.</p>
    <p class="body-copy">Lorem Ipsum is simply dummy text of the printing and typesetting industry. Lorem Ipsum has been the industry's standard dummy text ever since the 1500s, when an unknown printer took a galley of type and scrambled it to make a type specimen book.</p>
    <p class="body-copy">It has survived not only five centuries, but also the leap into electronic typesetting, remaining essentially unchanged. It was popularised in the 1960s with the release of Letraset sheets containing Lorem IpsumIpsum passages.</p>
    <p class="closing">Yours Sincerely</p>
    <p class="signatory">Marcus Ellory</p>
    <p class="role">Managing Director</p>
  </article>

  <svg class="footer-band" viewBox="0 0 1040 240" aria-hidden="true">
    <path d="M0,192 C300,196 600,196 760,188 C900,180 1010,120 1040,0 V240 H0 Z" fill="var(--orange)"/>
  </svg>
  <svg style="position:absolute;left:750px;top:975px;width:260px;height:175px" viewBox="0 0 260 175" role="img" aria-label="Decorative rising sun with rays">
    <defs>
      <radialGradient id="sunGlow" cx="65%" cy="90%" r="75%">
        <stop offset="0" stop-color="var(--orange)"/>
        <stop offset="1" stop-color="var(--sun-light)" stop-opacity="0"/>
      </radialGradient>
    </defs>
    <rect width="260" height="175" fill="url(#sunGlow)"/>
  </svg>

  <div class="sister-brand">KT Alarm</div>
  <div class="address">58, Harbour Row, Postcode 60418 Westmere</div>
</main>
</body>
</html>
```